Banner Ads for Online Poker Promotion

We are an online poker network, the KRX (www.thekrx.eu). We are looking for a small selection of web banner ads for our latest promotion and we are trying crowdsourcing for the first time!

Banner sizes that we need are:
- 196x523 (static .psd and .png)
- 199x129 (static .psd and .png)
- 447x426 (static .psd and .png)
- 500x400 (static .psd and .png)
- 697x167 (static .psd and .png)
- 460x60 (animated .gif)

The promotion name is ‘Late Rush’ and the concept is that a person who enters one of the specified tournaments four or more times during the promotion will win a free ticket to play that tournament again. So effectively a ‘Rush Late, Bag a Seat’ promo. We also are giving away €10,000 in free entries to the tournaments during the promotion. The specific tournaments are called ‘Calm Dawn Out’ and ‘The Sun Deck’ and run daily on our network. The promotion runs October 1 – 31.

Guidelines:

The name of the promotion, ‘Late Rush’, should feature prominently in the banners.

The strap line can be ‘Rush Late, Bag a Seat’ or something that encourages players to ‘take a shot’ at the tournaments.

Our network logo may feature, but is not absolutely necessary.

Examples of past promotional imagery can be found on our website, in particular these pages: http://www.thekrx.eu/promotions/ and http://www.thekrx.eu/promotions/archived-promotions/

We are looking to go in a more modern and risqué direction than the past, in order to stand out from competition which is very bland.

Please do not use common poker imagery – so no cards, chips, suit icons etc – or objects associated with live poker (tables, etc). This sort of imagery is too clichéd.

More like iOS7, less like iOS6

Think glamour, neon, rock music, extreme sports, and the Soft Tide!

If any further guidance is needed please don’t hesitate to ask.

```html
<!DOCTYPE html>
<html lang="en">
<head>
<meta charset="utf-8">
<title>Late Rush – Rush Late, Bag a Seat</title>
<link rel="stylesheet" href="https://fonts.googleapis.com/css2?family=Arimo:ital,wght@0,400;0,700;1,700&display=swap">
<style>
  :root {
    --brand-purple: #4b3d93;
    --brand-purple-light: #6a5cb8;
    --hot-pink: #ff1aa6;
    --ink: #111111;
    --paper: #ffffff;
    --paper-shade: #e9e9ee;
    --photo-light: #e8cdb8;
    --photo-mid: #d3a98a;
    --photo-hair: #e6cf95;
  }
  * { margin: 0; padding: 0; box-sizing: border-box; }
  html, body {
    width: 1200px;
    height: 960px;
    overflow: hidden;
    background: var(--paper);
  }
  .banner {
    position: relative;
    width: 500px;
    height: 400px;
    transform: scale(2.4);
    transform-origin: 0 0;
    overflow: hidden;
    font-family: "Arimo", Arial, sans-serif;
    background: linear-gradient(180deg, var(--paper) 60%, var(--paper-shade) 100%);
  }
  .header-band {
    position: absolute;
    inset: 0 0 auto 0;
    width: 500px;
    height: 90px;
  }
  .promo-title {
    position: absolute;
    left: 0;
    width: 500px;
    top: 8px;
    text-align: center;
    font-weight: 700;
    font-size: 96px;
    line-height: 1;
    letter-spacing: -1px;
    color: var(--hot-pink);
    text-shadow:
      -2px -2px 0 var(--paper), 2px -2px 0 var(--paper),
      -2px 2px 0 var(--paper), 2px 2px 0 var(--paper),
      0 3px 6px rgba(0,0,0,0.25);
  }
  .strapline {
    position: absolute;
    left: 0;
    width: 500px;
    top: 108px;
    text-align: center;
    font-weight: 400;
    font-size: 27px;
    color: var(--brand-purple);
  }
  .model-photo {
    position: absolute;
    left: 0;
    top: 150px;
    width: 235px;
    height: 250px;
    background:
      radial-gradient(ellipse 60% 55% at 55% 45%, var(--photo-light) 0%, var(--photo-mid) 55%, transparent 75%),
      linear-gradient(180deg, var(--photo-hair) 0%, #f3eee8 60%, var(--paper-shade) 100%);
  }
  .prize {
    position: absolute;
    left: 250px;
    width: 250px;
    top: 170px;
    text-align: center;
    color: var(--ink);
  }
  .prize-get {
    font-size: 50px;
    font-weight: 400;
    line-height: 1;
  }
  .prize-amount {
    font-size: 64px;
    font-weight: 400;
    line-height: 1.05;
    letter-spacing: -1px;
  }
  .prize-note {
    font-size: 11.5px;
    margin-top: 2px;
  }
  .cta {
    position: absolute;
    left: 233px;
    top: 318px;
    width: 256px;
    height: 60px;
  }
  .cta svg { position: absolute; inset: 0; }
  .cta-label {
    position: absolute;
    inset: 0;
    display: flex;
    align-items: center;
    justify-content: center;
    padding-left: 6px;
    font-style: italic;
    font-weight: 700;
    font-size: 21px;
    color: var(--paper);
    text-shadow: 0 1px 2px rgba(0,0,0,0.35);
  }
</style>
</head>
<body>
  <main class="banner">
    <svg class="header-band" viewBox="0 0 500 90" aria-hidden="true">
      <path d="M0 0 H500 V72 H338 L322 30 H0 Z" fill="var(--brand-purple)"/>
    </svg>

    <h1 class="promo-title">Late Rush</h1>
    <p class="strapline">Rush Late, Bag a Seat</p>

    <div class="model-photo" role="img" aria-label="Photo of a cheering blonde woman gesturing toward her head"></div>

    <section class="prize">
      <div class="prize-get">GET</div>
      <div class="prize-amount">€10,000</div>
      <div class="prize-note">in free entries to the tournaments</div>
    </section>

    <a class="cta" href="#">
      <svg viewBox="0 0 256 60" aria-hidden="true">
        <defs>
          <linearGradient id="ctaFill" x1="0" y1="0" x2="0" y2="1">
            <stop offset="0" stop-color="var(--brand-purple-light)"/>
            <stop offset="1" stop-color="var(--brand-purple)"/>
          </linearGradient>
        </defs>
        <path d="M10 2 H250 Q255 2 254 7 L246 53 Q245 58 240 58 H14 Q8 58 7 52 L2 8 Q1 2 10 2 Z" fill="url(#ctaFill)"/>
      </svg>
      <span class="cta-label">Start Playing Now</span>
    </a>
  </main>
</body>
</html>
```